HM Marketing Piece

Heron Meadow was created in 1984 as a shared aircraft ownership comprised of individual stockholders, interested in sharing the cost of aircraft ownership. Our strategy is simple, make owning and flying well maintained and upgraded aircraft more affordable through shared ownership.

When you own an aircraft individually, you have all the costs of a loan, hangar, insurance, subscriptions, annual inspection, and those unscheduled maintenance issues.

When you rent an aircraft from a local FBO, you get well used, dirty aircraft that everyone abuses with minimum hour requirements for weekend getaways that turn a 2 hour trip into a 9 hour hit on your wallet.

The solution? Shared aircraft ownership. Heron Meadow has three aircraft based out of Bramwell Field (KQLP). When you join a partnership, you split fixed costs between multiple individuals, AND get access to multiple well maintained and upgraded aircraft. When you fly, you pay the variable costs of your flight time only. Dividing the fixed expenses among multiple members makes flying much more affordable.

Benefits of shared aircraft ownership:

• Much cheaper than owning an aircraft individually
• Access to multiple aircraft
• Higher quality aircraft than your local FBO

• Hangared aircraft, flown by owners, not renters
• No overnight minimums
• On-line scheduling

www.heronmeadowfly.example

```html
<!DOCTYPE html>
<html lang="en">
<head>
<meta charset="utf-8">
<title>Heron Meadow – Shared Aircraft Ownership Mailer</title>
<link rel="stylesheet" href="https://fonts.googleapis.com/css2?family=Roboto:ital,wght@0,400;0,700;1,400&family=Roboto+Condensed:wght@400&display=swap">
<style>
  :root {
    --paper: #ffffff;
    --teal: #3bb5b0;
    --indigo: #48499a;
    --zone-pink: #f7bfc6;
    --trim-blue: #27a9e1;
    --ink: #231f20;
    --asphalt: #262425;
    --white: #ffffff;
  }
  html, body {
    margin: 0;
    padding: 0;
    width: 1200px;
    height: 930px;
    overflow: hidden;
    background: var(--paper);
  }
  .mailer {
    position: relative;
    width: 1200px;
    height: 930px;
    background: var(--paper);
    font-family: "Roboto", Arial, sans-serif;
    color: var(--ink);
  }
  .hero-photo {
    position: absolute;
    left: 30px;
    top: 30px;
    width: 873px;
    height: 870px;
    background:
      radial-gradient(ellipse 420px 300px at 560px 300px, rgba(255,255,255,1) 0%, rgba(255,255,255,0.95) 45%, rgba(255,255,255,0) 100%),
      radial-gradient(ellipse 260px 60px at 400px 370px, rgba(255,236,190,0.9) 0%, rgba(255,236,190,0) 100%),
      linear-gradient(to bottom,
        #8e8d8a 0px, #b4b3af 120px, #d8d7d3 230px, #cfd0cf 320px,
        #8d8a78 390px, #5c5b4a 450px, #4a4846 500px,
        #353334 560px, var(--asphalt) 640px, var(--asphalt) 870px);
  }
  .hero-photo::after {
    content: "";
    position: absolute;
    inset: 0;
    background: linear-gradient(to right, rgba(255,255,255,0) 0%, rgba(255,255,255,0) 50%, rgba(255,255,255,0.85) 80%, #fff 100%);
    clip-path: polygon(0 0, 100% 0, 100% 268px, 0 268px);
  }
  .zone {
    position: absolute;
    background: var(--zone-pink);
  }
  .zone--postage { left: 903px; top: 32px; width: 265px; height: 266px; }
  .zone--address { left: 580px; top: 298px; width: 588px; height: 470px; }
  .zone--barcode { left: 150px; top: 768px; width: 1018px; height: 129px; }
  .trim-line {
    position: absolute;
    left: 0; top: 0;
  }
  .headline {
    position: absolute;
    left: 62px;
    top: 98px;
    width: 810px;
    margin: 0;
    font-weight: 700;
    font-size: 72px;
    line-height: 1;
    letter-spacing: 10px;
    color: var(--teal);
    white-space: nowrap;
    overflow: hidden;
  }
  .headline-sub {
    position: absolute;
    right: 335px;
    top: 186px;
    margin: 0;
    font-style: italic;
    font-weight: 400;
    font-size: 48px;
    line-height: 1;
    color: var(--indigo);
  }
  .brand-name {
    position: absolute;
    left: 65px;
    top: 565px;
    margin: 0;
    font-family: "Roboto Condensed", "Arial Narrow", sans-serif;
    font-size: 24px;
    line-height: 1;
    color: var(--white);
  }
  .about {
    position: absolute;
    left: 65px;
    top: 626px;
    width: 483px;
    margin: 0;
    font-family: "Roboto Condensed", "Arial Narrow", sans-serif;
    font-size: 18px;
    line-height: 23.6px;
    color: var(--white);
  }
  .about-line {
    display: block;
    text-align: justify;
    text-align-last: justify;
    white-space: nowrap;
  }
  .about-line--last { text-align-last: left; }
  .zone-label {
    position: absolute;
    margin: 0;
    font-size: 35px;
    line-height: 43px;
    text-align: center;
    font-weight: 400;
  }
  .zone-label--postage { left: 903px; width: 265px; top: 120px; }
  .zone-label--address { left: 580px; width: 600px; top: 365px; }
  .zone-label--barcode { left: 150px; width: 1046px; top: 817px; }
  .zone-rules {
    position: absolute;
    left: 643px;
    top: 466px;
    width: 520px;
    margin: 0;
    font-size: 24.5px;
    line-height: 31px;
  }
</style>
</head>
<body>
<main class="mailer">
  <div class="hero-photo" role="img" aria-label="Photo of a small high-wing propeller aircraft on an airfield apron at sunset, a pilot standing beside it under a cloudy sky"></div>

  <div class="zone zone--postage"></div>
  <div class="zone zone--address"></div>
  <div class="zone zone--barcode"></div>

  <svg class="trim-line" width="1200" height="930" aria-hidden="true">
    <polyline points="903,32 1168,32 1168,897 150,897" fill="none" stroke="var(--trim-blue)" stroke-width="4"/>
  </svg>

  <h1 class="headline">SHARED AIRCRAFT</h1>
  <p class="headline-sub">ownership</p>

  <p class="brand-name">Heron Meadow</p>
  <p class="about">
    <span class="about-line">Heron Meadow Inc was Established in 1984 as a shared aircraft</span>
    <span class="about-line">ownership comprised of individual stockholders, interested in</span>
    <span class="about-line">sharing the cost of aircraft ownership. Our strategy is simple,</span>
    <span class="about-line">make owning and flying well maintained and upgraded aircraft</span>
    <span class="about-line about-line--last">more affordable through shared ownership.</span>
  </p>

  <p class="zone-label zone-label--postage">Postage<br>Area</p>
  <p class="zone-label zone-label--address">Address Area</p>
  <p class="zone-rules">The only text allowed in the Address Area<br>is the recipient mailing address.<br>Red zones may have no text or<br>graphics darker than 7% grayscale.</p>
  <p class="zone-label zone-label--barcode">Barcode Area</p>
</main>
</body>
</html>
```